HomeBridle business card and stationary design

We are looking for a simple yet elegant design for our mortgage company business card and stationary.

The card should include:
Name (Derek Walsh)
Title (CEO)
Phone Number (614-208-3917)
Address (48 Birchfield Court, Suite 314, Marlow, OH 43952)
Email (email@homebridle-example.com)
"NMLS" i.e. (NMLS 61947)
"Company NMLS" (Company NMLS 472815)

See above

```html
<!DOCTYPE html>
<html lang="en">
<head>
<meta charset="utf-8">
<title>HomeBridle Business Card</title>
<link rel="stylesheet" href="https://fonts.googleapis.com/css2?family=Montserrat:wght@500;600;700&family=Arimo:wght@400&display=swap">
<style>
  :root {
    --backdrop: #2a2a2a;
    --paper: #ffffff;
    --navy: #1b2733;
    --ink: #1d2530;
    --accent: #0ea5e9;
    --rule: #8a8f96;
  }
  * { margin: 0; padding: 0; box-sizing: border-box; }
  html, body {
    width: 1200px; height: 900px; overflow: hidden;
    background: var(--backdrop);
  }
  .canvas {
    width: 1200px; height: 900px;
    display: flex; flex-direction: column;
    align-items: center; justify-content: center; gap: 44px;
  }
  .card {
    width: 580px; height: 330px;
    position: relative;
    box-shadow: 0 14px 30px rgba(0,0,0,.45);
  }
  .card-front {
    background: var(--paper);
    border-bottom: 4px solid var(--accent);
    border-left: 3px solid var(--accent);
    font-family: "Arimo", Arial, sans-serif;
    color: var(--ink);
  }
  .identity {
    position: absolute; top: 58px; left: 0; right: 0;
    text-align: center;
  }
  .person-name {
    font-family: "Montserrat", sans-serif;
    font-weight: 700; font-size: 30px; letter-spacing: .2px;
    color: var(--ink);
  }
  .person-name .surname { color: var(--accent); }
  .person-title { font-size: 15px; margin-top: 2px; }
  .details {
    position: absolute; top: 150px; left: 0; right: 0;
    display: flex; justify-content: center; align-items: center; gap: 22px;
    font-size: 14px; line-height: 1.4;
  }
  .address { text-align: right; }
  .divider { width: 1px; height: 70px; background: var(--rule); }
  .contacts { list-style: none; }
  .contacts li { display: flex; align-items: center; gap: 6px; }
  .contacts svg { width: 13px; height: 13px; fill: var(--accent); flex: none; }
  .contacts .highlight { color: var(--accent); }
  .licenses {
    position: absolute; bottom: 34px; left: 0; right: 0;
    text-align: center; font-size: 14px;
  }
  .licenses .label { color: var(--accent); }
  .licenses .sep { margin: 0 8px; color: var(--ink); }
  .card-back {
    background: var(--navy);
    display: flex; align-items: center; justify-content: center;
  }
  .brand-name {
    font-family: "Montserrat", sans-serif;
    font-weight: 600; font-size: 60px; letter-spacing: 1px;
    color: #ffffff;
  }
</style>
</head>
<body>
<main class="canvas">
  <section class="card card-front" aria-label="Business card front">
    <header class="identity">
      <h1 class="person-name">Derek <span class="surname">Walsh</span></h1>
      <p class="person-title">CEO</p>
    </header>
    <div class="details">
      <address class="address" style="font-style:normal">
        48 Birchfield Court<br>Suite 314, Marlow<br>OH 43952
      </address>
      <span class="divider"></span>
      <ul class="contacts">
        <li>
          <svg viewBox="0 0 24 24" aria-hidden="true"><path d="M6.6 10.8a15.1 15.1 0 0 0 6.6 6.6l2.2-2.2c.3-.3.7-.4 1-.2 1.1.4 2.3.6 3.6.6.6 0 1 .4 1 1V20c0 .6-.4 1-1 1A17 17 0 0 1 3 4c0-.6.4-1 1-1h3.5c.6 0 1 .4 1 1 0 1.3.2 2.5.6 3.6.1.3 0 .7-.2 1z"/></svg>
          614-208-3917
        </li>
        <li>
          <svg viewBox="0 0 24 24" aria-hidden="true"><path d="M2 5h20v14H2zm2 2v.5l8 5 8-5V7zm0 3v7h16v-7l-8 5z"/></svg>
          email@homebridle-example.com
        </li>
        <li>
          <svg viewBox="0 0 24 24" aria-hidden="true"><path d="M12 2a10 10 0 1 0 0 20 10 10 0 0 0 0-20zm6.9 6h-2.9a15 15 0 0 0-1.4-3.9A8 8 0 0 1 18.9 8zM12 4c.8 1.2 1.5 2.5 1.9 4h-3.8c.4-1.5 1.1-2.8 1.9-4zM4.3 14a8 8 0 0 1 0-4h3.4a16 16 0 0 0 0 4zm.8 2h2.9c.3 1.4.8 2.7 1.4 3.9A8 8 0 0 1 5.1 16zM8 8H5.1a8 8 0 0 1 4.3-3.9C8.8 5.3 8.3 6.6 8 8zm4 12c-.8-1.2-1.5-2.5-1.9-4h3.8c-.4 1.5-1.1 2.8-1.9 4zm2.3-6H9.7a14 14 0 0 1 0-4h4.6a14 14 0 0 1 0 4zm.3 5.9c.6-1.2 1.1-2.5 1.4-3.9h2.9a8 8 0 0 1-4.3 3.9zm1.7-5.9a16 16 0 0 0 0-4h3.4a8 8 0 0 1 0 4z"/></svg>
          <span>www.<span class="highlight">homebridle</span>.com</span>
        </li>
      </ul>
    </div>
    <p class="licenses">
      <span class="label">NMLS</span> 61947<span class="sep">|</span><span class="label">Company NMLS</span> 472815
    </p>
  </section>

  <section class="card card-back" aria-label="Business card back">
    <p class="brand-name">HomeBridle</p>
  </section>
</main>
</body>
</html>
```